QRSTREAMHUB ( Wordpress website for catalogue of Lumigram Live Pages)

Need a website to showcase different Lumigram Live pages ( in different categories). Similar to e-commerce except no check-out / purchase of items. Pls use our logos provided and color scheme to be white+red+ blue as per our logo.
Updates

Target Market(s)

Consumers

Font styles to use
Sans Serif

Colors
ffffff
ec1f27
3276b5

Requirements
Must have
• I will need a Wordpress Theme as a handover. Also, pls use the color scheme (red+blue+white) as per logo attached. Prefer clean and near design with white space.

```html
<!DOCTYPE html>
<html lang="en">
<head>
<meta charset="utf-8">
<title>QRSTREAMHUB – Curated Lumigram Live Pages</title>
<link href="https://fonts.googleapis.com/css2?family=Lato:wght@400;700&family=Roboto+Condensed:wght@400;700&display=swap" rel="stylesheet">
<style>
:root{
  --red:#ec1f27;
  --blue:#2f6fb8;
  --blue-deep:#0e5bdc;
  --ink:#1d1d1d;
  --text:#4a4a4a;
  --grey:#f3f3f3;
  --line:#dcdcdc;
  --white:#ffffff;
}
*{box-sizing:border-box;margin:0;padding:0}
html,body{width:1200px;height:3041px;overflow:hidden;background:var(--white)}
body{position:relative;font-family:'Lato',sans-serif;color:var(--text)}
.abs{position:absolute}
.cond{font-family:'Roboto Condensed',sans-serif}
/* header */
.site-header{position:absolute;left:0;top:0;width:1200px;height:124px;background:var(--white)}
.brand{position:absolute;left:75px;top:43px;font-family:'Roboto Condensed',sans-serif;font-weight:700;font-size:38px;color:var(--blue-deep);letter-spacing:0.5px}
.search{position:absolute;left:874px;top:28px;width:252px;height:33px;border:1px solid var(--line);border-radius:17px;font-size:14px;color:#555;padding:8px 20px}
.search svg{position:absolute;right:14px;top:9px}
.nav{position:absolute;top:89px;right:74px;display:flex;gap:37px;font-size:13px;font-weight:700;color:#333;text-transform:uppercase}
.nav a{color:#333;text-decoration:none;padding:0 16px 10px;position:relative}
.nav a.active{color:var(--red)}
.nav a.active:after{content:"";position:absolute;left:0;right:0;bottom:-3px;height:3px;background:var(--red)}
/* hero */
.hero{position:absolute;left:0;top:124px;width:1200px;height:583px;background:linear-gradient(180deg,#efefef,#fafafa)}
.hero-art{position:absolute;left:470px;top:118px;width:712px;height:340px;border-radius:30px;background:linear-gradient(120deg,#dfe7f5,#c9d7f2 45%,#f1d5d6);z-index:1}
.hero-title{position:absolute;left:55px;top:183px;font-family:'Roboto Condensed',sans-serif;font-weight:700;font-size:72px;line-height:64px;color:var(--ink);letter-spacing:-2px;z-index:2;white-space:nowrap}
.hero-of{position:absolute;left:345px;top:170px;font-family:'Roboto Condensed',sans-serif;font-weight:700;font-style:italic;font-size:64px;line-height:64px;color:var(--red);z-index:3}
.hero-live{position:absolute;left:55px;top:392px;background:var(--red);color:var(--white);font-family:'Roboto Condensed',sans-serif;font-weight:700;font-size:62px;line-height:60px;padding:0 6px;border-radius:4px;z-index:2}
.band{position:absolute;left:0;top:707px;width:1200px;height:10px;background:linear-gradient(90deg,var(--red) 0 46%,var(--blue-deep) 46%)}
/* sections */
.ph{background:linear-gradient(135deg,#223049,#2c63c6 55%,#141b29)}
h2.sec{font-family:'Roboto Condensed',sans-serif;font-weight:700;font-size:28px;color:var(--blue);text-transform:uppercase}
.body{font-size:15px;line-height:27px;color:var(--text)}
.btn{position:absolute;background:var(--red);color:var(--white);border-radius:22px;font-family:'Lato',sans-serif;font-size:16px;text-align:center;line-height:44px;height:44px}
.btn.cond{font-family:'Roboto Condensed',sans-serif;font-weight:700;font-size:17px}
.grey{position:absolute;left:0;width:1200px;background:var(--grey)}
.center{position:absolute;left:0;width:1200px;text-align:center}
.card-title{font-family:'Roboto Condensed',sans-serif;font-weight:700;font-size:16px;color:var(--red);text-transform:uppercase}
.card-text{font-size:15px;line-height:23px}
.feat{position:absolute;top:1758px;width:326px;height:356px;border:1px solid var(--line);background:var(--white)}
.feat .pic{position:absolute;left:42px;top:14px;width:240px;height:184px}
.feat h3{position:absolute;left:0;width:100%;top:210px;text-align:center;font-weight:400;font-size:19px;color:var(--blue)}
.feat p{position:absolute;left:0;width:100%;top:240px;text-align:center;font-size:15px;color:#333}
.feat .btn{left:72px;top:288px;width:180px}
.cat{position:absolute;top:2346px;width:330px}
.cat .box{height:195px;background:var(--white);position:relative}
.cat .pic{position:absolute;left:48px;top:9px;width:235px;height:176px}
.cat h3{margin-top:36px;text-align:center;font-family:'Roboto Condensed',sans-serif;font-weight:700;font-size:17px;color:var(--blue)}
.cat p{margin-top:10px;text-align:center;font-size:14px;color:#444}
.arrow{position:absolute}
/* footer */
.footer{position:absolute;left:0;top:2790px;width:1200px;height:251px;background:var(--blue-deep);color:var(--white)}
.footer h4{font-family:'Roboto Condensed',sans-serif;font-weight:700;font-size:16px;text-transform:uppercase;position:absolute;top:60px}
.footer ul{list-style:none;position:absolute;top:94px;font-size:13px;line-height:27px}
.f-brand{position:absolute;left:75px;top:60px;font-family:'Roboto Condensed',sans-serif;font-weight:700;font-size:40px;color:var(--white)}
.f-copy{position:absolute;left:75px;top:121px;font-size:12px;line-height:20px}
.socials{position:absolute;left:75px;top:176px;display:flex;gap:18px}
.socials span{width:20px;height:20px;border-radius:50%;background:var(--white);opacity:.95}
.email{position:absolute;left:885px;top:96px;width:241px;height:37px;background:var(--white);border-radius:19px;color:#444;font-size:12px;padding:11px 0 0 50px}
.email svg{position:absolute;left:18px;top:13px}
.signup{position:absolute;left:1037px;top:155px;width:89px;height:36px;border-radius:18px;background:var(--red);font-size:13px;font-weight:700;text-align:center;line-height:36px}
</style>
</head>
<body>

<header class="site-header">
  <div class="brand">QRSTREAMHUB</div>
  <div class="search">Search..
    <svg width="13" height="13" viewBox="0 0 13 13"><circle cx="5.5" cy="5.5" r="4.2" fill="none" stroke="#222" stroke-width="2"/><line x1="8.5" y1="8.5" x2="12" y2="12" stroke="#222" stroke-width="2"/></svg>
  </div>
  <nav class="nav">
    <a class="active">Home</a><a>Lumigram Lives happening now!</a><a>Feature Lumigram Lives</a><a>Categories</a><a>Contact us</a>
  </nav>
</header>

<section class="hero">
  <div class="hero-art" role="img" aria-label="Illustration of a phone streaming a live sale next to two shoppers with bags and boxes in a store"></div>
  <div class="hero-title">A PORTAL<br>CURATED<br>LUMIGRAM</div>
  <div class="hero-of">of</div>
  <div class="hero-live">LIVE</div>
</section>
<div class="band"></div>

<section>
  <div class="abs ph" style="left:75px;top:770px;width:512px;height:330px" role="img" aria-label="Photo of a hand holding a phone showing the Lumigram app"></div>
  <h2 class="sec abs" style="left:615px;top:778px">Welcome to our website</h2>
  <p class="body abs" style="left:615px;top:826px;width:490px">Aliquam molestie, mi et imperdiet euismod, dui purus auctor tellus, et interdum lacus lectus et ante. Sed accumsan sollicitudin sapien, sit amet adipiscing turpis gravida ac. In congue, neque ac lobortis volutpat, libero mauris varius mi, vitae suscipit ipsum ligula vitae risus. Duis aliquam nibh a dui iaculis.<br>viverra id a velit. Vivamus egestas risus in magna varius commodo etiam pretium porttitor lectus..</p>
  <div class="btn" style="left:615px;top:1036px;width:181px">READ MORE</div>
</section>

<section class="grey" style="top:1166px;height:480px">
  <h2 class="sec center" style="top:64px">Lumigram Lives happening now!</h2>
  <div class="abs" style="left:75px;top:126px;width:330px;height:189px;background:linear-gradient(135deg,#8a7a5c,#3d3a35)" role="img" aria-label="Photo of people in a cafe with a laptop open on a sign-up page"></div>
  <div class="abs" style="left:436px;top:126px;width:330px;height:189px;background:linear-gradient(135deg,#bcb6ae,#4d4f5e)" role="img" aria-label="Photo of shelves stocked with kitchen appliances"></div>
  <div class="abs" style="left:797px;top:126px;width:330px;height:189px;background:linear-gradient(135deg,#d9c592,#9a6a3e)" role="img" aria-label="Photo of hands holding phones with floating social reaction icons"></div>
  <div class="abs" style="left:75px;top:343px;width:330px;text-align:center"><div class="card-title">Duis aliquam nibh a dui</div><p class="card-text" style="margin-top:6px">Aliquam molestie, mi et imperdiet euismod,<br>dui purus auctor tellus et.</p></div>
  <div class="abs" style="left:436px;top:343px;width:330px;text-align:center"><div class="card-title">Duis aliquam nibh a dui</div><p class="card-text" style="margin-top:6px">Aliquam molestie, mi et imperdiet euismod, dui<br>purus auctor tellus et.</p></div>
  <div class="abs" style="left:797px;top:343px;width:330px;text-align:center"><div class="card-title">Duis aliquam nibh a dui</div><p class="card-text" style="margin-top:6px">Aliquam molestie, mi et imperdiet euismod, dui<br>purus auctor tellus et.</p></div>
</section>

<section>
  <h2 class="sec center" style="top:1692px">Featured Lumigram Lives</h2>
  <svg class="arrow" style="left:38px;top:1918px" width="22" height="42" viewBox="0 0 22 42"><polyline points="20,1 2,21 20,41" fill="none" stroke="#888" stroke-width="2"/></svg>
  <svg class="arrow" style="left:1140px;top:1918px" width="22" height="42" viewBox="0 0 22 42"><polyline points="2,1 20,21 2,41" fill="none" stroke="#888" stroke-width="2"/></svg>
  <div class="feat" style="left:75px"><div class="pic" style="background:linear-gradient(135deg,#c9b79a,#8c4b35)" role="img" aria-label="Grid of food product listing photos"></div><h3>Duis in auctor sapien</h3><p>Maecenas in sem sed elit vulputate</p><div class="btn cond">READ MORE</div></div>
  <div class="feat" style="left:438px"><div class="pic" style="background:linear-gradient(135deg,#b8a35a,#b52a25)" role="img" aria-label="Grid of fresh fruit photos"></div><h3>Duis in auctor sapien</h3><p>Maecenas in sem sed elit vulputate</p><div class="btn cond">READ MORE</div></div>
  <div class="feat" style="left:801px"><div class="pic" style="background:linear-gradient(135deg,#e8d6d8,#8fb8d8)" role="img" aria-label="Grid of plush hair accessory photos"></div><h3>Duis in auctor sapien</h3><p>Maecenas in sem sed elit vulputate</p><div class="btn cond">READ MORE</div></div>
</section>

<section class="grey" style="top:2185px;height:605px">
  <h2 class="sec center" style="top:55px">Categories</h2>
  <p class="center" style="top:110px;font-size:14px;color:#333">Aliquam molestie, mi et imperdiet euismod, dui purus auctor tellus, et interdum lacus lectus et ante.</p>
  <svg class="arrow" style="left:38px;top:260px" width="22" height="42" viewBox="0 0 22 42"><polyline points="20,1 2,21 20,41" fill="none" stroke="#888" stroke-width="2"/></svg>
  <svg class="arrow" style="left:1140px;top:260px" width="22" height="42" viewBox="0 0 22 42"><polyline points="2,1 20,21 2,41" fill="none" stroke="#888" stroke-width="2"/></svg>
</section>
<div class="cat" style="left:75px"><div class="box"><div class="pic" style="background:linear-gradient(135deg,#8a8580,#3a3530)" role="img" aria-label="Photo of a store shelf of speakers and gadgets"></div></div><h3>DOLOREM IPSUM</h3><p>Maecenas in sem sed elit vulputate</p></div>
<div class="cat" style="left:434px"><div class="box"><div class="pic" style="background:linear-gradient(135deg,#e8d6d8,#8fb8d8)" role="img" aria-label="Grid of plush hair accessory photos"></div></div><h3>DOLOREM IPSUM</h3><p>Maecenas in sem sed elit vulputate</p></div>
<div class="cat" style="left:795px"><div class="box"><div class="pic" style="background:linear-gradient(135deg,#a05060,#4a6078)" role="img" aria-label="Grid of clothing photos"></div></div><h3>DOLOREM IPSUM</h3><p>Maecenas in sem sed elit vulputate</p></div>
<div class="btn cond" style="left:481px;top:2684px;width:238px">VIEW ALL CATEGORIES</div>

<footer class="footer">
  <div class="f-brand">QRSTREAMHUB</div>
  <div class="f-copy">Copyright © 2020. Company Name.<br>All Right Reserved</div>
  <div class="socials"><span></span><span></span><span></span><span></span><span></span></div>
  <h4 style="left:390px">Quick links</h4>
  <ul style="left:390px"><li>Home</li><li>Lumigram LIVEs happening now!</li><li>Feature Lumigram Lives</li><li>Categories</li><li>Contact us</li></ul>
  <h4 style="left:634px">Contact info</h4>
  <ul style="left:634px;font-size:12px;line-height:24px">
    <li>42 Harbour Lane</li><li>Northvale, NV 20418</li>
    <li><svg width="12" height="12" viewBox="0 0 12 12" style="margin-right:20px"><path d="M2 1h3l1 3-2 1c1 2 2 3 4 4l1-2 3 1v3c-6 0-10-4-10-10z" fill="#fff"/></svg>1-800-555-0148</li>
    <li><svg width="12" height="9" viewBox="0 0 12 9" style="margin-right:20px"><rect width="12" height="9" fill="#fff"/><polyline points="0,0 6,5 12,0" fill="none" stroke="#0e5bdc"/></svg>hello@qrstreamhub.example</li>
  </ul>
  <h4 style="left:885px">Email sign up</h4>
  <div class="email"><svg width="12" height="9" viewBox="0 0 12 9"><rect width="12" height="9" fill="#333"/><polyline points="0,0 6,5 12,0" fill="none" stroke="#fff"/></svg>Enter Email Address</div>
  <div class="signup">SIGN UP</div>
</footer>

</body>
</html>
```